Corvale Clinic New Branding Stationary Set - updated Oct 30th 2017

Updated on 30th Oct 2017 as we now need a whole folder design instead of a folder cover. We have thought out exactly what should be on it so it wont be hard. We are happy for this to be completed only by the winning designer if you like. And also we are guaranteeing this project now. Thanks!

We just got our new logo and now we would like a stationary set so we can brand our company communications. The items we need designed are:
Business cards
Letterhead
Appointment confirmation cards
Folder - switched from folder cover. Note that if you don't wish to do this unless you are selected as the winner this is fine.

1. Business cards - for 5 employees, final names will be given once the winner is selected, but you can use this one as the sample:
Lucinda Prieto
Hair Regrowth Expert
Corvale Clinic
7127 Marbury Ave, Suite 500
Kestrel Park CA 90877
lucinda@gavinthorpemd.example
(555) 238-9016

2. Letterhead 8.5" x 11.0" vertical
Corvale Clinic
Kestrel Park CA 90877
office@corvaleclinic.example
(555) 238-9016

3. Appointment Confirmation cards - business card size
Corvale Clinic
Kestrel Park CA 90877
Appointment For:
Date:
Time:
If you are unable to make your appointment, please contact us to reschedule at:
(555) 238-9016
info@gavinthorpemd.example

*UPDATED*
4. Folder 9" x 12 " vertical with double pocket
We would like the infinity image from the logo made really big so the left side is on the back and the right side with the + sign is on the front and its takes up the maximum room on the folder.
On the front below the half logo it should say "A Biochemical Revolution..."
On the inside we would also like to have the infinity sign from the logo but faded and half on the left pocket half on the right.
On left inside pocket it should say (this will be partically written on top of the logo):
Gavin Thorpe MD
Precision Medicine
Halt and Thicken Hair
On the Right inside pocket it should say the following:
Because the Enemy of BETTER Health is Good Health
BETTER Ingredients
BETTER Recipe
BETTER Medicine
On the back below the logo on the bottom should be the contact information.
I attached a picture of our drawing of what we want for this to make it easier.

Here is our website to give you an idea of our branding: http://www.haltandthicken.example/

We are the only true cure for hair loss and need to look professional and highest quality and beyond reproach from an ethical standpoint. We are a medical clinic so this should be portrayed also.
We cured hair loss by analyzing biochemistry and rebalancing it so that the process reverses and your own hair can grow back naturally.

Business card information:

OK so here is the information for the business cards:

Lucinda Prieto
Hair Regrowth Expert
(555) 238-9016
www.corvaleclinic.example

Marisol Quintero
Hair Growth Consultant
(555) 238-9016
marisol@gavinthorpemd.example
www.corvaleclinic.example

Glenda Hutchins
CMO/COO
(555) 238-9016
glenda@haltandthicken.example
www.corvaleclinic.example

Dr Lou Thorpe
President
(555) 238-9016
info@gavinthorpemd.example
www.corvaleclinic.example

Corvale Clinic
Customer Service
(555) 238-9016
info@gavinthorpemd.example
www.corvaleclinic.example

Target Market(s)

Men aged 20-24 who care about their appearance, care about their hair and care about the world.

Industry/Entity Type

Medical And Science

Font styles to use
Sans Serif

Colors
00a990
ffffff
9d9d9d
333333

Requirements
Must have
• Must use the logo and our brand colors from the logo in all designs.
• The pantone colors are:
• Green: #4ca26f
• Light Grey: #999999
• The design should be symmetrical and balanced.
Nice to have
• It should look reasonably masculine.
Should not have
• Do not include any red in the design.

```html
<!DOCTYPE html>
<html lang="en">
<head>
<meta charset="utf-8">
<title>Corvale Clinic — Letterhead</title>
<link href="https://fonts.googleapis.com/css2?family=Open+Sans:wght@400;600;700&display=swap" rel="stylesheet">
<style>
  :root {
    --backdrop: #0e0c2a;
    --paper: #ffffff;
    --brand-green: #4cd64c;
    --brand-grey: #999999;
    --ink: #222222;
    --rule: #333333;
  }
  * { margin: 0; padding: 0; box-sizing: border-box; }
  html, body {
    width: 937px; height: 1200px; overflow: hidden;
    background: var(--backdrop);
    font-family: "Open Sans", Arial, sans-serif;
  }
  .canvas { position: relative; width: 937px; height: 1200px; }
  .letterhead {
    position: absolute; left: 118px; top: 106px;
    width: 700px; height: 987px;
    background: var(--paper); overflow: hidden;
  }
  .brand-mark {
    position: absolute; left: 106px; top: 96px;
    display: flex; align-items: center; gap: 9px;
  }
  .brand-mark .dot {
    width: 16px; height: 16px; border-radius: 50%;
    background: var(--brand-green);
  }
  .brand-mark .name {
    font-weight: 700; font-size: 17px; letter-spacing: 0.3px;
    color: var(--brand-grey); text-transform: uppercase; white-space: nowrap;
  }
  .divider {
    position: absolute; left: 409px; top: 51px;
    width: 1.5px; height: 121px; background: var(--rule);
  }
  .contact {
    position: absolute; left: 424px; top: 77px;
    font-size: 11.5px; line-height: 15px; color: var(--ink);
  }
  .contact .company { color: var(--brand-green); font-weight: 600; }
  .contact .line { display: flex; align-items: center; gap: 6px; }
  .contact .icon {
    width: 10px; height: 10px; border-radius: 50%;
    background: var(--brand-green); display: inline-flex;
    align-items: center; justify-content: center;
  }
  .side-tab {
    position: absolute; right: 0; top: 80px;
    width: 8px; height: 51px; background: var(--brand-green);
  }
  .footer-band {
    position: absolute; left: 266px; right: 0; bottom: 0;
    height: 34px; background: var(--brand-green);
    color: var(--paper); font-size: 12px;
    display: flex; align-items: center; justify-content: center;
    padding-left: 30px;
  }
  .footer-cap {
    position: absolute; left: 172px; bottom: 0;
    width: 112px; height: 34px; background: var(--paper);
    border-radius: 0 17px 17px 0;
    display: flex; align-items: center; justify-content: center; gap: 5px;
  }
  .footer-cap .dot {
    width: 9px; height: 9px; border-radius: 50%; background: var(--brand-green);
  }
  .footer-cap .name {
    font-size: 8px; font-weight: 700; color: var(--brand-grey);
    text-transform: uppercase; white-space: nowrap;
  }
</style>
</head>
<body>
<div class="canvas">
  <div class="letterhead">
    <div class="brand-mark">
      <span class="dot"></span>
      <span class="name">Corvale Clinic</span>
    </div>

    <div class="divider"></div>

    <div class="contact">
      <div class="company">Corvale Clinic</div>
      <div>7127 Marbury Ave, Suite 500</div>
      <div>Kestrel Park CA 90877</div>
      <div class="line">
        <span class="icon">
          <svg width="6" height="6" viewBox="0 0 6 6"><rect x="1.5" y="0.5" width="3" height="5" rx="0.6" fill="#fff"/></svg>
        </span>
        <span>(555) 238-9016</span>
      </div>
      <div class="line">
        <span class="icon">
          <svg width="6" height="5" viewBox="0 0 6 5"><rect x="0.3" y="0.5" width="5.4" height="4" fill="#fff"/><path d="M0.3 0.6 L3 2.6 L5.7 0.6" stroke="#4cd64c" stroke-width="0.6" fill="none"/></svg>
        </span>
        <span>office@corvaleclinic.example</span>
      </div>
    </div>

    <div class="side-tab"></div>

    <div class="footer-band">www.corvaleclinic.example</div>
    <div class="footer-cap">
      <span class="dot"></span>
      <span class="name">Corvale Clinic</span>
    </div>
  </div>
</div>
</body>
</html>
```